Long Established Local Fencing (not swords) Business needs fresh Business Cards

We need fresh double sided business cards for our Fencing Construction business, we are looking for something with our new logo design added, and maybe a photo background ?
We recently had cards made from Quillmarko and we were horrified with what we got back, the quality was terrible, so am looking for high quality format for good printing company to make.
We install Steelwave, Timber paling, Aluminium Slat Screening, Picket (timber and aluminium) and most other fencing installations.
Our website is brelbanfencing.com.au should you like to learn a bit more.
We do have logo in other formats if required.
We have been in business for over 35 years and we have used this as a "motto" it is on our signage

Industry/Entity Type

Construction

Contact Information for Business Card

Open to ideas, we need 3 x different cards, one generic with no name and 2 x others each with 1 of our bosses name on each, I will put into upload files.

Colors
ec1f27
000000
606060
f5f5f5

Requirements
Must have
• Company Name and Logo
• Address
• Contact details, phone, website, email etc
• Small space to write notes when leaving card at residence
Nice to have
• Our motto "Servicing the Peninsula for over 35 years"

```html
<!DOCTYPE html>
<html lang="en">
<head>
<meta charset="utf-8">
<title>Brelban Fencing – General Card</title>
<link href="https://fonts.googleapis.com/css2?family=Open+Sans:wght@400;700;800&family=Rochester&display=swap" rel="stylesheet">
<style>
  :root {
    --red: #ec1f27;
    --black: #000000;
    --grey: #606060;
    --light: #f5f5f5;
    --white: #ffffff;
    --bronze: #6b2a12;
  }
  html, body { margin: 0; padding: 0; overflow: hidden; background: var(--white); }
  .sheet { position: relative; width: 988px; height: 1200px; overflow: hidden; font-family: "Open Sans", sans-serif; color: var(--black); }
  .card { position: absolute; left: 0; width: 988px; height: 565px; overflow: hidden; background: var(--white); }
  .card--front { top: 0; }
  .card--back { top: 635px; }
  .card svg.bg { position: absolute; inset: 0; }
  .sheet-label { position: absolute; top: 580px; left: 0; width: 988px; text-align: center; font-size: 40px; font-weight: 400; }

  .brand { position: absolute; display: flex; align-items: center; gap: 14px; }
  .brand__mark { width: 26px; height: 26px; background: var(--red); flex: none; }
  .brand__name { font-weight: 800; font-size: 50px; line-height: 1.02; text-transform: uppercase; color: var(--black); letter-spacing: 1px; }

  .front-brand { left: 555px; top: 185px; }
  .abn { position: absolute; left: 635px; top: 305px; font-size: 14px; }
  .rule { position: absolute; left: 485px; top: 325px; width: 468px; height: 4px; background: var(--red); }
  .address { position: absolute; left: 487px; top: 333px; font-size: 30px; }
  .contacts { position: absolute; left: 490px; top: 410px; margin: 0; padding: 0; list-style: none; }
  .contacts li { display: flex; align-items: center; gap: 12px; height: 39px; font-size: 28px; }
  .contacts .icon { width: 30px; height: 30px; background: var(--red); display: flex; align-items: center; justify-content: center; flex: none; }

  .back-brand { left: 90px; top: 230px; }
  .back-brand .brand__name { font-size: 48px; }
  .back-web { position: absolute; left: 40px; top: 490px; font-size: 29px; }
  .motto { position: absolute; right: 38px; top: 80px; text-align: right; font-family: "Rochester", cursive; font-size: 46px; line-height: 0.98; }
  .motto span { display: block; }
  .motto .accent { color: var(--red); }
  .notes { position: absolute; left: 485px; top: 285px; width: 460px; }
  .notes div { height: 56px; border-bottom: 3px dotted var(--black); }
</style>
</head>
<body>
<main class="sheet">

  <section class="card card--front">
    <svg class="bg" width="988" height="565" viewBox="0 0 988 565">
      <defs>
        <linearGradient id="silver" x1="0" x2="1" y1="0" y2="0">
          <stop offset="0" stop-color="#8e8e92"/>
          <stop offset="0.3" stop-color="#e8e8ea"/>
          <stop offset="0.55" stop-color="#a9a9ad"/>
          <stop offset="0.8" stop-color="#f1f1f3"/>
          <stop offset="1" stop-color="#9c9ca0"/>
        </linearGradient>
        <linearGradient id="photoTone" x1="0" x2="0" y1="0" y2="1">
          <stop offset="0" stop-color="#a8c28a"/>
          <stop offset="0.5" stop-color="#8ea67a"/>
          <stop offset="1" stop-color="#4d5d8a"/>
        </linearGradient>
      </defs>
      <path d="M0 0 H470 Q405 280 470 565 H0 Z" fill="url(#silver)"/>
      <path d="M470 0 Q405 280 470 565 L462 565 Q395 280 458 0 Z" fill="var(--bronze)"/>
      <rect x="38" y="35" width="362" height="493" fill="url(#photoTone)" role="img" aria-label="Photo collage of installed fences: steel sheet fence with lattice top, aluminium pool fencing and a blue panel fence"/>
    </svg>
    <div class="brand front-brand">
      <div class="brand__mark"></div>
      <div class="brand__name">Brelban<br>Fencing</div>
    </div>
    <div class="abn">ABN 12 345 67 890</div>
    <div class="rule"></div>
    <div class="address"># Po Box 512, Marrowvale NSW 2290</div>
    <ul class="contacts">
      <li><span class="icon"><svg width="18" height="18" viewBox="0 0 24 24"><path d="M6 2h4l2 5-3 2a11 11 0 0 0 6 6l2-3 5 2v4c0 1-1 2-2 2A18 18 0 0 1 4 4c0-1 1-2 2-2z" fill="#fff"/></svg></span>(02)4 555 0184</li>
      <li><span class="icon"><svg width="20" height="16" viewBox="0 0 20 16"><rect x="1" y="1" width="18" height="14" fill="none" stroke="#fff" stroke-width="2"/><path d="M1 1l9 8 9-8" fill="none" stroke="#fff" stroke-width="2"/></svg></span>brelbanfencing@mailpond.com</li>
      <li><span class="icon"><svg width="20" height="20" viewBox="0 0 20 20"><circle cx="10" cy="10" r="8" fill="none" stroke="#fff" stroke-width="2"/><path d="M2 10h16M10 2c-4 5-4 11 0 16M10 2c4 5 4 11 0 16" fill="none" stroke="#fff" stroke-width="1.6"/></svg></span>www.brelbanfencing.com.au</li>
    </ul>
  </section>

  <div class="sheet-label">General Card</div>

  <section class="card card--back">
    <svg class="bg" width="988" height="565" viewBox="0 0 988 565">
      <defs>
        <linearGradient id="silver2" x1="0" x2="1" y1="0" y2="0">
          <stop offset="0" stop-color="#8a8a8e"/>
          <stop offset="0.35" stop-color="#ececee"/>
          <stop offset="0.6" stop-color="#a4a4a8"/>
          <stop offset="0.85" stop-color="#eeeef0"/>
          <stop offset="1" stop-color="#9a9a9e"/>
        </linearGradient>
        <linearGradient id="fadePhoto" x1="0" x2="0" y1="0" y2="1">
          <stop offset="0" stop-color="#f4f5f6"/>
          <stop offset="0.5" stop-color="#e6e8e8"/>
          <stop offset="1" stop-color="#dfe2df"/>
        </linearGradient>
      </defs>
      <rect x="430" y="0" width="558" height="565" fill="url(#fadePhoto)" role="img" aria-label="Faded photo of a cream steel panel fence along a driveway"/>
      <path d="M0 0 H505 Q420 280 475 565 H0 Z" fill="url(#silver2)"/>
    </svg>
    <div class="brand back-brand">
      <div class="brand__mark"></div>
      <div class="brand__name">Brelban<br>Fencing</div>
    </div>
    <div class="back-web">www.brelbanfencing.com.au</div>
    <div class="motto">
      <span>Servicing the Peninsula</span>
      <span class="accent">for over 30 years</span>
    </div>
    <div class="notes"><div></div><div></div><div></div><div></div><div></div></div>
  </section>

</main>
</body>
</html>
```